Asphalt Paving Specialists Business Cards

Our company is TREVIN ASPHALT. We need a business cards two of our asphalt paving team members. We're asphalt specialists.
I need two made up please. The details on the front of the each business card i would like please is as follows.
Address is 87 Marrowby St, Clontarf, QLD, 4019.

Company Director
Gordon Pelliway
gord@trevinpave.com.au
04 58 736 042
www.trevinpave.com.au

Supervisor
Curtis Vonnegard
curtis@trevinpave.com.au
0462 873 105
www.trevinpave.com.au

We do all aspects of Asphalt Paving. Specific Services include - Driveways, Carparks & sub-divisions. All Roads. Repairs and Maintenance.

We provide free quotes!

I dont have a certain way i want them to look so im open to all designs :)

** I have uploaded our logo for the TREVIN ASPHALT. HOWEVER, CAN YOU PLEASE GET RID OF THE ( PTY LTD )

Thank you
Renata Fulch
TREVIN ASPHALT

Target Market(s)

Home owners and Business Owners

Contact Information for Business Card

Asphalt Paving Specialists. All aspects of Asphalt. Residential, Commercial & Industrial. Based in Brisbane.

Font styles to use
Sans Serif

Colors

Designer to choose colors to be used in the design.

Requirements
Nice to have
• maybe an image of a driveway? or Asphalt?

```html
<!DOCTYPE html>
<html lang="en">
<head>
<meta charset="utf-8">
<title>Trevin Asphalt – Business Card</title>
<link href="https://fonts.googleapis.com/css2?family=Roboto:wght@300;400;500;700&display=swap" rel="stylesheet">
<style>
  :root {
    --page-bg: #dcd7d2;
    --card-light: #eef0f1;
    --card-mist: #d5dde3;
    --blue-top: #2a97ec;
    --blue-mid: #1978c4;
    --blue-deep: #0c4f86;
    --edge-line: #111418;
    --road-tone: #a3a5a8;
    --name-ink: #0f1d2b;
    --white: #ffffff;
    --peach: #f3dcb2;
    --brand-ink: #0d3a63;
    --icon-ink: #0d1620;
    --icon-detail: #5c8fbf;
  }
  * { margin: 0; padding: 0; box-sizing: border-box; }
  html, body {
    width: 1200px;
    height: 1120px;
    overflow: hidden;
    background: var(--page-bg);
    font-family: "Roboto", "Helvetica Neue", Arial, sans-serif;
  }
  .business-card {
    position: absolute;
    left: 60px;
    top: 251px;
    width: 1080px;
    height: 617px;
    overflow: hidden;
    background: linear-gradient(120deg, var(--card-light) 0%, var(--card-mist) 100%);
    box-shadow: 0 0 0 1px rgba(255,255,255,0.7), 0 10px 30px rgba(0,0,0,0.18);
  }
  .card-art {
    position: absolute;
    inset: 0;
    width: 1080px;
    height: 617px;
  }
  .holder {
    position: absolute;
    left: 54px;
    color: var(--white);
  }
  .holder-name {
    top: 82px;
    font-size: 33px;
    font-weight: 500;
    color: var(--name-ink);
  }
  .holder-title {
    top: 124px;
    font-size: 24px;
    font-weight: 300;
    letter-spacing: 0.3px;
  }
  .contact-list {
    position: absolute;
    left: 54px;
    top: 196px;
    list-style: none;
  }
  .contact-item {
    display: flex;
    align-items: center;
    height: 35.5px;
    font-size: 24px;
    font-weight: 400;
    color: var(--white);
  }
  .contact-icon {
    width: 26px;
    height: 22px;
    margin-right: 19px;
    flex: none;
  }
  .services-intro {
    position: absolute;
    left: 54px;
    top: 329px;
    font-size: 24px;
    line-height: 32px;
    font-weight: 400;
    color: var(--peach);
  }
  .services-list {
    position: absolute;
    left: 54px;
    top: 428px;
    list-style: none;
  }
  .services-list li {
    font-size: 24px;
    line-height: 32.5px;
    color: var(--white);
  }
  .services-list li::before {
    content: "•";
    display: inline-block;
    width: 20px;
    font-size: 16px;
    vertical-align: 3px;
  }
  .brand-name {
    position: absolute;
    left: 575px;
    top: 274px;
    font-size: 40px;
    font-weight: 700;
    letter-spacing: 1px;
    color: var(--brand-ink);
  }
</style>
</head>
<body>
  <section class="business-card">
    <svg class="card-art" viewBox="0 0 1080 617" xmlns="http://www.w3.org/2000/svg">
      <defs>
        <linearGradient id="panelBlue" x1="0" y1="0" x2="0.6" y2="1">
          <stop offset="0" stop-color="var(--blue-top)"/>
          <stop offset="0.55" stop-color="var(--blue-mid)"/>
          <stop offset="1" stop-color="var(--blue-deep)"/>
        </linearGradient>
        <linearGradient id="roadTone" x1="0" y1="0" x2="1" y2="0">
          <stop offset="0" stop-color="var(--road-tone)" stop-opacity="0.55"/>
          <stop offset="0.6" stop-color="var(--road-tone)" stop-opacity="0.3"/>
          <stop offset="1" stop-color="var(--road-tone)" stop-opacity="0"/>
        </linearGradient>
      </defs>
      <rect class="road-illustration" x="330" y="0" width="660" height="617" fill="url(#roadTone)"
            role="img" aria-label="Illustration of a winding asphalt road with dashed centre line"/>
      <path class="info-panel" d="M0,0 H830 C620,30 470,110 455,200 C440,280 560,300 540,380 C515,480 380,560 245,617 H0 Z"
            fill="url(#panelBlue)"/>
      <path class="panel-edge" d="M830,0 C620,30 470,110 455,200 C440,280 560,300 540,380 C515,480 380,560 245,617"
            fill="none" stroke="var(--edge-line)" stroke-width="5"/>
    </svg>

    <h1 class="holder holder-name">Gordon Pelliway</h1>
    <p class="holder holder-title">COMPANY DIRECTOR</p>

    <ul class="contact-list">
      <li class="contact-item">
        <svg class="contact-icon" viewBox="0 0 26 22"><path d="M2,7 C6,1 20,1 24,7 L21,10 L17,8 L17,5 C14,4 12,4 9,5 L9,8 L5,10 Z M7,11 H19 L22,20 H4 Z" fill="var(--icon-ink)"/><circle cx="13" cy="15.5" r="2.5" fill="var(--icon-detail)"/></svg>
        04 58 736 042
      </li>
      <li class="contact-item">
        <svg class="contact-icon" viewBox="0 0 26 22"><rect x="2" y="4" width="22" height="15" fill="var(--icon-ink)"/><path d="M2,4 L13,13 L24,4" fill="none" stroke="var(--icon-detail)" stroke-width="1.6"/></svg>
        gord@trevinpave.com.au
      </li>
      <li class="contact-item">
        <svg class="contact-icon" viewBox="0 0 26 22"><circle cx="13" cy="11" r="10" fill="var(--icon-ink)"/><path d="M8,6 C11,7 10,10 13,11 C15,12 12,16 14,19 M17,4 C16,7 19,8 21,9" fill="none" stroke="var(--icon-detail)" stroke-width="2"/></svg>
        www.trevinpave.com.au
      </li>
    </ul>

    <p class="services-intro">We do all aspects&nbsp; of Asphalt Paving.<br>Specific Services</p>

    <ul class="services-list">
      <li>Driveways</li>
      <li>Carparks &amp; sub-divisions</li>
      <li>All Roads</li>
      <li>Repairs &amp; Maintenance</li>
    </ul>

    <p class="brand-name">TREVIN ASPHALT</p>
  </section>
</body>
</html>
```